Dental Business Card Design w/logo

Classic, elegant w/a touch of contemporary
Upscale dental facility located in Modesto CA
Specializing in restorative & general dentistry
Providing exceptional customer service to the community
Updates

I prefer script and not bold writing
If you can use the phone; fax and email icons instead of spelling them out, it would be great
No bold colors
Classy and elegant
In the back of the card I would like to see something like this
Your Next Appointment:
Mon     Tue    Wed    Thur (a box next to each of them for marking)
Date:_______________ at_____________ AM    PM  (a box next to them for marking)

Thank you

Target Market(s)

Well established professional

Industry/Entity Type

Dental

Contact Information for Business Card

Velorine Tamsuki DMD
4176 Larchmont Rd
Suite D7
Modesto, CA 95368

Office: 209-731-5092
Fax: 209-731-8247
Email: tamsukidmd@brivelmail.test

Requirements
Must have
• Unique classic logo
An easily repeatable design that can be used on letterhead and envelopes
Nice to have
• My initials incorporated into unique design
Should not have
• No cartoons or cheesy themes. This is a practice for the well established and professional individual.

```html
<!DOCTYPE html>
<html lang="en">
<head>
<meta charset="utf-8">
<title>Velorine Tamsuki DMD — Business Card</title>
<link rel="stylesheet" href="https://fonts.googleapis.com/css2?family=Cinzel:wght@400&family=Noto+Serif:wght@400&display=swap">
<style>
  :root {
    --backdrop: #8a8a8a;
    --card: #ffffff;
    --ink: #1f1f1f;
    --frame: #6e665b;
    --accent: #8a7658;
  }
  * { margin: 0; padding: 0; box-sizing: border-box; }
  html, body {
    width: 1200px;
    height: 810px;
    overflow: hidden;
    background: var(--backdrop);
  }
  .stage {
    width: 1200px;
    height: 810px;
    display: flex;
    align-items: center;
    justify-content: center;
  }
  .card {
    position: relative;
    width: 840px;
    height: 480px;
    background: var(--card);
    box-shadow: 0 2px 10px rgba(0,0,0,0.18);
  }
  .card-frame {
    position: absolute;
    inset: 0;
    width: 100%;
    height: 100%;
  }
  .card-content {
    position: absolute;
    inset: 0;
    display: flex;
    flex-direction: column;
    align-items: center;
    text-align: center;
    color: var(--ink);
  }
  .doctor-name {
    margin-top: 72px;
    font-family: "Cinzel", serif;
    font-weight: 400;
    font-size: 38px;
    letter-spacing: 2px;
    line-height: 1;
  }
  .doctor-credential {
    margin-top: 6px;
    font-family: "Cinzel", serif;
    font-size: 20px;
    letter-spacing: 3px;
  }
  .practice-mark {
    margin-top: 40px;
    display: flex;
    align-items: center;
    gap: 12px;
    font-family: "Cinzel", serif;
    font-size: 30px;
    letter-spacing: 2px;
    color: var(--ink);
  }
  .practice-mark-dot {
    width: 12px;
    height: 12px;
    border-radius: 50%;
    background: var(--accent);
  }
  .contact {
    margin-top: auto;
    margin-bottom: 62px;
    font-family: "Noto Serif", serif;
    font-size: 18px;
    line-height: 1.45;
    letter-spacing: 1.2px;
  }
  .contact-label { color: var(--accent); }
  .contact-gap { display: inline-block; width: 14px; }
  .contact-email { font-size: 17px; }
</style>
</head>
<body>
  <main class="stage">
    <article class="card">
      <svg class="card-frame" viewBox="0 0 840 480" aria-hidden="true">
        <path d="M42,20 H798 A22,22 0 0 0 820,42 V438 A22,22 0 0 0 798,460 H42 A22,22 0 0 0 20,438 V42 A22,22 0 0 0 42,20 Z"
              fill="none" stroke="var(--frame)" stroke-width="1.6"/>
        <path d="M44,28 H796 A16,16 0 0 0 812,44 V436 A16,16 0 0 0 796,452 H44 A16,16 0 0 0 28,436 V44 A16,16 0 0 0 44,28 Z"
              fill="none" stroke="var(--frame)" stroke-width="0.9"/>
      </svg>
      <div class="card-content">
        <h1 class="doctor-name">Velorine Tamsuki</h1>
        <p class="doctor-credential">DMD</p>
        <div class="practice-mark">
          <span class="practice-mark-dot"></span>
          <span class="practice-mark-name">Tamsuki</span>
        </div>
        <address class="contact" style="font-style: normal;">
          <div class="contact-phones">
            <span class="contact-label">Office:</span> 209 - 731 - 5092<span class="contact-gap"></span><span class="contact-label">Fax:</span> 209 - 731 - 8247
          </div>
          <div class="contact-address">4176 Larchmont Rd Suite D7 Modesto, CA 95368</div>
          <div class="contact-email"><span class="contact-label">Email:</span> tamsukidmd@brivelmail.test</div>
        </address>
      </div>
    </article>
  </main>
</body>
</html>
```